Contemporary Elegant Business Card Design for an International Trade Company in the Wine Industry

We need a new business card design for an international trade company in the wine and winemaking industry. The overall feel of the card should be contemporary, upscale, luxurious and elegant. It should communicate confidence and professionalism. The colors should complementary to our logo design (burgundy, gold, and black).
Inspiration: rich velvet tapestry
The card should include the following information:
Business: Brovenna Trading/Shipping, LLC.
Name: Marcus T. Hollenbrand
Title: CEO
Email: mark@brovennatrading.example
Phone: 555-294-6172
www.brovennatrading.example
Updates
Project Deadline Extended
Reason: We'd like the designers that we requested some additional designs from to still submit designs. Thank you!
Industry/Entity Type
Business
Contact Information for Business Card
Title: CEO
Phone: 555-294-6172
www.brovennatrading.example
Look and feel

```html
<!DOCTYPE html>
<html lang="en">
<head>
<meta charset="utf-8">
<title>Brovenna Trading/Shipping – Business Card</title>
<link href="https://fonts.googleapis.com/css2?family=Open+Sans:wght@400;600&display=swap" rel="stylesheet">
<style>
  :root {
    --burgundy: #6e1118;
    --burgundy-deep: #5a0d14;
    --gold: #e0a63a;
    --gold-light: #e8b957;
    --map-light: #e3a94c;
    --map-dark: #9a5a1f;
    --ink: #ffffff;
    --stage: #2b2624;
  }
  * { margin: 0; padding: 0; box-sizing: border-box; }
  html, body {
    width: 1200px; height: 720px; overflow: hidden;
    background: var(--stage);
    font-family: "Open Sans", Arial, sans-serif;
  }
  .canvas { position: relative; width: 1200px; height: 720px; }
  .card {
    position: absolute; top: 205px;
    width: 540px; height: 310px;
    background: var(--burgundy);
    overflow: hidden;
    box-shadow: 0 10px 28px rgba(0,0,0,.55);
  }
  .card--front { left: 45px; }
  .card--back { left: 615px; }
  .card__map { position: absolute; inset: 0; width: 100%; height: 100%; }

  .front-brand {
    position: absolute; left: 34px; top: 38px;
    color: var(--gold);
    font-weight: 600;
  }
  .front-brand__name { font-size: 46px; letter-spacing: 1px; line-height: 1; }
  .front-brand__tag { font-size: 12px; letter-spacing: 1.5px; margin-top: 6px; text-transform: uppercase; }

  .contact {
    position: absolute; left: 170px; top: 118px; color: var(--ink);
    white-space: nowrap;
  }
  .contact__name {
    color: var(--gold-light); font-weight: 600;
    font-size: 18px; line-height: 24px; margin-left: 74px;
  }
  .contact__title {
    display: flex; align-items: center; gap: 8px;
    font-size: 13px; line-height: 18px;
  }
  .contact__rule { width: 170px; height: 1px; background: var(--ink); }
  .contact__list { list-style: none; margin-top: 6px; font-size: 13px; line-height: 20px; }
  .contact__list li { display: flex; align-items: center; gap: 8px; }
  .contact__list svg { width: 11px; height: 11px; fill: var(--gold-light); flex: none; }

  .company-band {
    position: absolute; left: 22px; bottom: 36px;
    width: 300px; height: 26px;
    background: var(--gold);
    clip-path: polygon(0 0, 100% 0, 93% 100%, 0 100%);
    color: var(--burgundy-deep);
    font-size: 13px; line-height: 26px; padding-left: 14px;
    white-space: nowrap;
  }

  .back-brand {
    position: absolute; right: 24px; bottom: 32px;
    display: flex; align-items: center; gap: 10px;
    color: var(--ink); font-weight: 600; font-size: 22px; line-height: 26px; letter-spacing: 1px;
  }
  .back-brand__mark { width: 18px; height: 18px; background: var(--gold); }
</style>
</head>
<body>
<main class="canvas">

  <section class="card card--front" aria-label="Business card front">
    <svg class="card__map" viewBox="0 0 540 310" preserveAspectRatio="none">
      <defs>
        <linearGradient id="mapFront" x1="0" y1="0" x2="1" y2="1">
          <stop offset="0" stop-color="#e3a94c"/>
          <stop offset="1" stop-color="#9a5a1f"/>
        </linearGradient>
      </defs>
      <polygon role="img" aria-label="Antique world map in warm gold and brown tones"
               points="300,0 540,0 540,310" fill="url(#mapFront)"/>
    </svg>
    <div class="front-brand">
      <div class="front-brand__name">BROVENNA</div>
      <div class="front-brand__tag">Trading and Shipping</div>
    </div>
  </section>

  <section class="card card--back" aria-label="Business card back">
    <svg class="card__map" viewBox="0 0 540 310" preserveAspectRatio="none">
      <defs>
        <linearGradient id="mapBack" x1="0" y1="0" x2="1" y2="1">
          <stop offset="0" stop-color="#9a5a1f"/>
          <stop offset="0.6" stop-color="#e3a94c"/>
        </linearGradient>
      </defs>
      <polygon role="img" aria-label="Antique world map in warm gold and brown tones"
               points="0,0 420,0 0,230" fill="url(#mapBack)"/>
    </svg>

    <div class="contact">
      <div class="contact__name">Marcus T. Hollenbrand</div>
      <div class="contact__title">CEO <span class="contact__rule"></span></div>
      <ul class="contact__list">
        <li><svg viewBox="0 0 24 24"><path d="M6.6 10.8a15 15 0 0 0 6.6 6.6l2.2-2.2a1 1 0 0 1 1-.25 11.4 11.4 0 0 0 3.6.57 1 1 0 0 1 1 1V20a1 1 0 0 1-1 1A17 17 0 0 1 3 4a1 1 0 0 1 1-1h3.5a1 1 0 0 1 1 1c0 1.25.2 2.45.57 3.57a1 1 0 0 1-.25 1z"/></svg>555-294-6172</li>
        <li><svg viewBox="0 0 24 24"><path d="M2 5h20v14H2z M2 5l10 8 10-8" stroke="#6e1118" stroke-width="1.5"/></svg>mark@brovennatrading.example</li>
        <li><svg viewBox="0 0 24 24"><circle cx="12" cy="12" r="10"/></svg>www.brovennatrading.example</li>
      </ul>
    </div>

    <div class="company-band">Brovenna Trading / Shipping, LLC</div>

    <div class="back-brand">
      <span class="back-brand__mark"></span>
      <span>BROVENNA</span>
    </div>
  </section>

</main>
</body>
</html>
```